Rack Card Design Project

www.northlodgefreightway.com I am looking for a Rack Card for our Pick up/drop off and shipping purposes. So listed below are things I want on it.
Name, Address, Phone number, Credit Card info, Pickup or Drop off location, What the Item is, How many pieces or boxes. We are a hunting/ fishing company that specializes in Cold Storage and shipping of peoples fish and animals from Alaska. I added our company logo and also a Design of a Rack card so you can see what we are looking for.

```html
<!DOCTYPE html>
<html lang="en">
<head>
<meta charset="utf-8">
<title>North Lodge Freightway – Pick Up / Drop Off Rack Card</title>
<link href="https://fonts.googleapis.com/css2?family=Graduate&family=Roboto:wght@400;500&display=swap" rel="stylesheet">
<style>
  :root {
    --red: #b5121b;
    --black: #1c1c1c;
    --white: #ffffff;
    --ink: #3a3a3a;
    --line: #2b2b2b;
    --backdrop: #e6e6e6;
  }
  html, body {
    margin: 0;
    width: 1200px;
    height: 1200px;
    overflow: hidden;
    background: var(--backdrop);
  }
  .rack-card {
    position: absolute;
    left: 346px;
    top: 50px;
    width: 507px;
    height: 1100px;
    background: var(--white);
    font-family: "Roboto", Arial, sans-serif;
    color: var(--ink);
  }
  .striped-band {
    position: absolute;
    left: 0;
    width: 507px;
    background: linear-gradient(to right,
      var(--black) 0 22px, var(--white) 22px 33px, var(--black) 33px 43px, var(--white) 43px 54px,
      var(--red) 54px 453px,
      var(--white) 453px 464px, var(--black) 464px 474px, var(--white) 474px 485px, var(--black) 485px 507px);
    display: flex;
    align-items: center;
    justify-content: center;
    overflow: hidden;
  }
  .header-band { top: 0; height: 128px; }
  .footer-band { top: 1034px; height: 66px; }
  .rule {
    position: absolute;
    left: 0;
    width: 507px;
    height: 6px;
    background: var(--black);
  }
  .header-rule { top: 133px; }
  .footer-rule { top: 1022px; }
  .card-title {
    margin: 0;
    font-family: "Graduate", "Roboto Slab", serif;
    font-weight: 400;
    color: var(--white);
    font-size: 42px;
    line-height: 1.08;
    text-align: center;
    letter-spacing: 0;
    white-space: nowrap;
    transform: scaleX(0.7);
    -webkit-text-stroke: 1px var(--white);
  }
  .website {
    font-size: 15px;
    letter-spacing: 4px;
    color: var(--white);
    padding-left: 6px;
  }
  .field {
    position: absolute;
    box-sizing: border-box;
    border: 2px solid var(--line);
    font-size: 15.5px;
    padding: 9px 9px;
  }
  .checkbox-option {
    position: absolute;
    top: 471px;
    display: flex;
    align-items: center;
    gap: 9px;
    font-size: 16px;
  }
  .checkbox-option .box {
    width: 19px;
    height: 19px;
    box-sizing: border-box;
    border: 1.5px solid var(--ink);
  }
  .brand-block {
    position: absolute;
    top: 862px;
    left: 0;
    width: 507px;
    display: flex;
    flex-direction: column;
    align-items: center;
    gap: 10px;
  }
  .brand-art {
    width: 180px;
    height: 92px;
    background: linear-gradient(135deg, #7a4a2a 0%, #9b6b45 40%, #8c8f96 70%, #c8463f 100%);
    border-radius: 6px;
  }
  .brand-name {
    font-family: "Roboto", Arial, sans-serif;
    font-weight: 500;
    font-size: 17px;
    letter-spacing: 1.5px;
    color: var(--black);
  }
</style>
</head>
<body>
  <main class="rack-card">
    <header class="striped-band header-band">
      <h1 class="card-title">PICK UP/DROP OFF AND<br>SHIPPING PURPOSES</h1>
    </header>
    <div class="rule header-rule"></div>

    <div class="field" style="left:29px; top:156px; width:274px; height:41px;">Name:</div>
    <div class="field" style="left:308px; top:156px; width:168px; height:41px;">Date:&nbsp;&nbsp;&nbsp;&nbsp;&nbsp;&nbsp;&nbsp;&nbsp;/&nbsp;&nbsp;&nbsp;&nbsp;/</div>
    <div class="field" style="left:29px; top:213px; width:447px; height:129px;">Address:</div>
    <div class="field" style="left:29px; top:355px; width:448px; height:41px;">Phone number:</div>
    <div class="field" style="left:29px; top:414px; width:290px; height:41px;">Credit Card no:</div>
    <div class="field" style="left:317px; top:414px; width:160px; height:41px;">Exp:</div>

    <div class="checkbox-option" style="left:41px;"><span class="box"></span>Veltra</div>
    <div class="checkbox-option" style="left:158px;"><span class="box"></span>Maxicard</div>

    <div class="field" style="left:30px; top:511px; width:447px; height:128px;">Pickup location:</div>
    <div class="field" style="left:30px; top:652px; width:447px; height:128px;">Drop location:</div>
    <div class="field" style="left:29px; top:799px; width:448px; height:41px;">How many pieces or boxes:</div>

    <div class="brand-block">
      <div class="brand-art" role="img" aria-label="Illustration area: Alaskan wildlife scene with moose, mountain sheep on a peak and salmon"></div>
      <div class="brand-name">NORTH LODGE FREIGHTWAY</div>
    </div>

    <div class="rule footer-rule"></div>
    <footer class="striped-band footer-band">
      <span class="website">www.northlodgefreightway.com</span>
    </footer>
  </main>
</body>
</html>
```